Web Developer Needs a Business Card Design

I need a personal business card design that represents me as a web developer for potential employers. I would like the background to be a dark color on the front for contrast with my logo and name. The back will have all my information along with a smaller version of the logo. I want something with a modern look and feel, not too conservative. This will be used for potential employers and freelance work.

Industry/Entity Type

Business

Contact Information for Business Card

Front should have my logo and name. The back should have all my personal information which would include: name: Tom Brevardi, phone: 570-614-9083, email: tombrevardi@mailwisp.com, website url: www.tombrevardi.com, logo, web developer.

Font styles to use
Sans Serif

Requirements
Must have
• Must include my logo. The color palette base color will be the logo color.

```html
<!DOCTYPE html>
<html lang="en">
<head>
<meta charset="utf-8">
<title>Tom Brevardi — Web Developer Business Card</title>
<link rel="stylesheet" href="https://fonts.googleapis.com/css2?family=Open+Sans:wght@400;700&display=swap">
<style>
  :root {
    --mint: #8ccbb8;
    --charcoal: #383838;
    --paper: #ffffff;
  }
  * { margin: 0; padding: 0; box-sizing: border-box; }
  html, body {
    width: 1200px;
    height: 686px;
    overflow: hidden;
    background: var(--paper);
  }
  .card {
    position: relative;
    width: 1200px;
    height: 686px;
    background: var(--paper);
    font-family: "Open Sans", Arial, sans-serif;
  }
  .band-top {
    position: absolute;
    left: 0; top: 0;
    width: 100%;
    height: 77px;
    background: var(--mint);
  }
  .band-dark {
    position: absolute;
    left: 0; top: 77px;
    width: 100%;
    height: 51px;
    background: var(--charcoal);
  }
  .brand-mark {
    position: absolute;
    left: 506px;
    top: 234px;
    width: 200px;
    height: 200px;
  }
  .identity {
    position: absolute;
    left: 0;
    top: 456px;
    width: 100%;
    text-align: center;
  }
  .name {
    color: var(--mint);
    font-weight: 700;
    font-size: 54px;
    line-height: 64px;
    letter-spacing: 1px;
    text-transform: uppercase;
  }
  .role {
    margin-top: 2px;
    color: var(--charcoal);
    font-weight: 400;
    font-size: 30px;
    line-height: 40px;
    text-transform: uppercase;
  }
</style>
</head>
<body>
  <main class="card">
    <div class="band-top"></div>
    <div class="band-dark"></div>

    <svg class="brand-mark" viewBox="0 0 200 200" aria-label="Tom Brevardi">
      <circle cx="100" cy="100" r="92" fill="none" stroke="var(--mint)" stroke-width="15"/>
      <text x="100" y="108" text-anchor="middle"
            font-family="Open Sans, Arial, sans-serif" font-weight="700"
            font-size="22" fill="var(--mint)">Tom Brevardi</text>
    </svg>

    <div class="identity">
      <h1 class="name">Tom Brevardi</h1>
      <p class="role">Web Developer</p>
    </div>
  </main>
</body>
</html>
```